Pelin Thai Massage Double Sided Flyer Luxury

I require a double sided flyer
we are a Thai Massage Spa
Would like gold, deep purple and bronze colours
Something eye catching and looks professional

```html
<!DOCTYPE html>
<html lang="en">
<head>
<meta charset="utf-8">
<title>Pelin Thai Massage – Double Sided Flyer</title>
<link href="https://fonts.googleapis.com/css2?family=Cinzel:wght@400;500&family=Lato:wght@300;400&family=Roboto+Condensed:wght@300;400&display=swap" rel="stylesheet">
<style>
  :root{
    --stage:#d8d8d8;
    --brown-deep:#2a170d;
    --brown:#3a2214;
    --brown-band:#24140b;
    --gold:#c9a13f;
    --gold-light:#ecd77e;
    --gold-text:#d9a845;
    --cream:#f6efe0;
    --ink:#f1ebe1;
  }
  *{margin:0;padding:0;box-sizing:border-box}
  html,body{width:1200px;height:854px;overflow:hidden;background:var(--stage)}
  body{position:relative;font-family:"Lato",sans-serif;color:var(--ink)}
  .flyer{position:absolute;top:100px;width:460px;height:652px;overflow:hidden;
    background:linear-gradient(180deg,var(--brown) 0%,var(--brown-deep) 100%);
    box-shadow:0 6px 18px rgba(0,0,0,.35)}
  .flyer--front{left:107px}
  .flyer--back{left:622px}
  .flyer svg.shapes{position:absolute;inset:0}
  .abs{position:absolute}

  .brand{position:absolute;text-align:center;width:220px;font-size:17px;color:var(--gold-text);font-weight:400;letter-spacing:.2px}
  .brand-mark{position:absolute;width:44px;height:44px;border-radius:50%;border:2px solid var(--gold)}

  .welcome{left:83px;top:349px;width:302px;height:29px;border-radius:14px;
    background:linear-gradient(90deg,#8a6a1f,#e9d27a 35%,#c9a13f 70%,#7a5a18);
    font-family:"Cinzel",serif;font-size:19px;color:#2a170d;text-align:center;line-height:29px;letter-spacing:1px}
  .intro{left:26px;right:26px;text-align:center;font-size:13.2px;line-height:17px;font-weight:400}

  .contact{left:22px;font-size:14px;display:flex;align-items:center;gap:9px}
  .contact .ico{width:17px;height:17px;border-radius:50%;background:#e3a72c;display:flex;align-items:center;justify-content:center}
  .badge{left:339px;top:515px;width:92px;height:92px;border-radius:50%;
    background:radial-gradient(circle at 45% 40%,#4a2c18,#24140b);
    border:2px solid var(--gold);box-shadow:0 0 0 3px #24140b,0 0 0 4px #8a6a1f,0 3px 8px rgba(0,0,0,.5);
    display:flex;align-items:center;justify-content:center;text-align:center}
  .badge span{transform:rotate(9deg);font-size:13.5px;line-height:15px;letter-spacing:.5px;color:var(--cream);text-transform:uppercase}
  .open{right:13px;top:622px;font-size:12.5px;color:var(--gold-text);display:flex;align-items:center;gap:5px}

  .section-title{right:12px;top:256px;font-family:"Cinzel",serif;font-size:22px;color:var(--gold-text);letter-spacing:1px}
  .tagline{right:12px;top:284px;font-size:12.5px;color:var(--gold-text)}
  .lede{right:12px;top:300px;width:230px;text-align:center;font-size:11.3px;line-height:14px}

  .treat-icon{position:absolute;top:366px;width:40px;height:40px;border-radius:50%;
    background:var(--cream);box-shadow:0 0 0 2px #8a6a1f}
  .treat-title{font-family:"Roboto Condensed",sans-serif;font-weight:300;font-size:15.5px;text-align:center;width:200px;line-height:19px;text-transform:uppercase}
  .price{font-family:"Roboto Condensed",sans-serif;width:204px}
  .price-row{display:flex;align-items:baseline;font-size:13px;font-weight:300}
  .price-row .dots{flex:1;border-bottom:1px dotted var(--ink);margin:0 2px 3px}
  .price-note{font-size:10px;font-weight:300;line-height:13px;margin-bottom:11px}

  .book{left:0;right:0;top:588px;text-align:center;font-size:15.5px;color:var(--gold-text);display:flex;justify-content:center;align-items:center;gap:6px}
  .web{left:0;right:0;top:615px;text-align:center;font-size:14px}
</style>
</head>
<body>

<!-- Front side -->
<section class="flyer flyer--front">
  <svg class="shapes" width="460" height="652" viewBox="0 0 460 652">
    <defs>
      <linearGradient id="frontPhoto" x1="0" y1="0" x2="1" y2="1">
        <stop offset="0" stop-color="#f4e8d8"/><stop offset=".5" stop-color="#c98a55"/><stop offset="1" stop-color="#8a4f2a"/>
      </linearGradient>
      <linearGradient id="goldLine" x1="0" x2="1">
        <stop offset="0" stop-color="#8a6a1f"/><stop offset=".5" stop-color="#f1dd7f"/><stop offset="1" stop-color="#b8902f"/>
      </linearGradient>
    </defs>
    <rect width="460" height="260" fill="url(#frontPhoto)" role="img" aria-label="Photo of a woman relaxing during a back massage beside candles and spa décor"/>
    <path d="M0,248 C120,232 200,176 300,180 C380,184 420,208 460,214 L460,652 L0,652 Z" fill="#33200f"/>
    <path d="M0,246 C120,230 200,174 300,178 C380,182 420,206 460,212" fill="none" stroke="url(#goldLine)" stroke-width="4"/>
    <path d="M3,553 C50,535 90,520 130,522 C200,526 270,585 350,592" fill="none" stroke="url(#goldLine)" stroke-width="4"/>
  </svg>

  <div class="brand-mark" style="left:208px;top:240px"></div>
  <div class="brand" style="left:120px;top:316px">Pelin Thai Massage</div>

  <div class="abs welcome">Welcome to Luxury</div>

  <p class="abs intro" style="top:396px">Set in the heart of Roundhay, Pelin Thai Massage will allow you to immerse yourself in a place where your wellbeing and rejuvenation is at the centre of what we do.</p>
  <p class="abs intro" style="top:465px">Using Thai traditions, our highly trained therapists offer revitalising body treatments with their deep tissue massage techniques. In their hands, you will see and feel immediate results.</p>

  <div class="abs contact" style="top:566px">
    <span class="ico"><svg width="10" height="10" viewBox="0 0 24 24"><path d="M6.6 10.8a15 15 0 0 0 6.6 6.6l2.2-2.2a1 1 0 0 1 1-.25 11 11 0 0 0 3.6.6 1 1 0 0 1 1 1V20a1 1 0 0 1-1 1A17 17 0 0 1 3 4a1 1 0 0 1 1-1h3.5a1 1 0 0 1 1 1 11 11 0 0 0 .6 3.6 1 1 0 0 1-.25 1z" fill="#2a170d"/></svg></span>
    0113 496 0721
  </div>
  <div class="abs contact" style="top:594px">
    <span class="ico"><svg width="12" height="12" viewBox="0 0 24 24" fill="none" stroke="#2a170d" stroke-width="2"><circle cx="12" cy="12" r="9"/><path d="M3 12h18M12 3c3 3.5 3 14.5 0 18M12 3c-3 3.5-3 14.5 0 18"/></svg></span>
    www.pelinthaimassage.co.uk
  </div>
  <div class="abs contact" style="top:622px">
    <span class="ico"><svg width="9" height="11" viewBox="0 0 24 30"><path d="M12 0a10 10 0 0 0-10 10c0 7.5 10 20 10 20s10-12.5 10-20A10 10 0 0 0 12 0zm0 14a4 4 0 1 1 0-8 4 4 0 0 1 0 8z" fill="#2a170d"/></svg></span>
    42 Birch Row Leeds LS8 9ZT
  </div>

  <div class="abs badge"><span>Gift<br>Vouchers<br>Available</span></div>

  <div class="abs open">
    <svg width="12" height="12" viewBox="0 0 24 24" fill="none" stroke="currentColor" stroke-width="2"><rect x="3" y="5" width="18" height="16" rx="2"/><path d="M3 10h18M8 3v4M16 3v4"/></svg>
    OPEN 7 DAYS A WEEK
  </div>
</section>

<!-- Back side -->
<section class="flyer flyer--back">
  <svg class="shapes" width="460" height="652" viewBox="0 0 460 652">
    <defs>
      <linearGradient id="backPhoto" x1="0" y1="0" x2="1" y2="0">
        <stop offset="0" stop-color="#efe2d2"/><stop offset=".45" stop-color="#e2b98f"/><stop offset="1" stop-color="#a97a4c"/>
      </linearGradient>
      <linearGradient id="goldLine2" x1="0" x2="1">
        <stop offset="0" stop-color="#8a6a1f"/><stop offset=".35" stop-color="#f1dd7f"/><stop offset="1" stop-color="#b8902f"/>
      </linearGradient>
    </defs>
    <rect width="460" height="260" fill="url(#backPhoto)" role="img" aria-label="Photo of a woman receiving a relaxing facial massage beside a bamboo mat and candles"/>
    <path d="M0,214 C40,187 80,176 120,181 C200,191 260,250 330,247 C390,244 430,222 460,212 L460,652 L0,652 Z" fill="#33200f"/>
    <path d="M0,212 C40,185 80,174 120,179 C200,189 260,248 330,245 C390,242 430,220 460,210" fill="none" stroke="url(#goldLine2)" stroke-width="4"/>
    <rect x="0" y="348" width="460" height="227" fill="#2e1a0e"/>
    <line x1="0" y1="348" x2="460" y2="348" stroke="#5a3a20" stroke-width="1.5"/>
    <rect x="0" y="575" width="460" height="77" fill="var(--brown-band)"/>
    <line x1="0" y1="575" x2="460" y2="575" stroke="#5a3a20" stroke-width="1.5"/>
  </svg>

  <div class="brand-mark" style="left:95px;top:236px"></div>
  <div class="brand" style="left:7px;top:309px">Pelin Thai Massage</div>

  <h2 class="abs section-title">MASSAGES</h2>
  <div class="abs tagline">Restore balance. Revive your senses.</div>
  <p class="abs lede">Discover all the ways Pelin Thai Massage can breathe new life into your body and soul.</p>

  <span class="treat-icon" style="left:45px"></span>
  <span class="treat-icon" style="left:97px"></span>
  <span class="treat-icon" style="left:150px"></span>
  <span class="treat-icon" style="left:270px"></span>
  <span class="treat-icon" style="left:323px"></span>
  <span class="treat-icon" style="left:376px"></span>

  <h3 class="abs treat-title" style="left:17px;top:428px">Deep Tissue Massage</h3>
  <h3 class="abs treat-title" style="left:243px;top:428px">Thai Floor Tradtional<br>Massage</h3>

  <div class="abs price" style="left:18px;top:477px">
    <div class="price-row"><span>60 minutes</span><span class="dots"></span><span>£45</span></div>
    <div class="price-note">Oil massage personalised, light to firm pressure</div>
    <div class="price-row"><span>90 minutes</span><span class="dots"></span><span>£55</span></div>
    <div class="price-note">Oil massage, medium to firm pressure</div>
  </div>
  <div class="abs price" style="left:243px;top:477px">
    <div class="price-row"><span>60 minutes</span><span class="dots"></span><span>£45</span></div>
    <div class="price-note">Dry massage, medium to firm pressure applying stretching technique</div>
  </div>

  <div class="abs book">
    Please call for appointment
    <svg width="15" height="15" viewBox="0 0 24 24" fill="none" stroke="currentColor" stroke-width="2"><circle cx="12" cy="12" r="10"/><path d="M9 7l1.5 3-1.2 1.2a7 7 0 0 0 3.5 3.5L14 13.5l3 1.5-.5 2a8 8 0 0 1-9.5-9.5z" fill="currentColor" stroke="none"/></svg>
    0113 496 0721
  </div>
  <div class="abs web">www.pelinthaimassage.co.uk</div>
</section>

</body>
</html>
```